Employees at R&T Gale Power Services need new modern business cards

We need new business cards that showcase our new rebranded logo. We are seeking modern, clean, fresh, attractive cards while still being professional. We want to stand out. A little bit about us: we work in Canada and the USA. We offer Technical Field Advisors to support wind turbine manufacturers through the construction phase of wind farms. I am attaching a mock inspiration picture to lead you in the direction we want to see this go. Also, FYI We have approx. 10/11 different employees that would need their own card. Let me know when you would need everyone's name. We would love to see some black and white options as well as color copies- when using colors we want green to be the dominant color with accents for blue and orange (colors should match our logo). I have also attached copies of our old business card for reference.

Contact Information for Business Card

Name, Telephone, Email, address, company name, website. EXAMPLE: Dean Whitlock, DeanWhitlock@randtgale.net, 555-384-9162, 318276 Fallow Line #7, Marrowby, ON X9Z 4Q2, www.randtgale.net

Colors
0054AA
0677BA
7BADD7
CADEEF
E8F1F8
00AB8E
00BBA5
67D7C9
C6EFE9
E9F9F6
F0912C
F2A743
F7CA91
FBE8D2
FDF5EE

Requirements
Must have
• 2 sided business card

```html
<!DOCTYPE html>
<html lang="en">
<head>
<meta charset="utf-8">
<title>R&amp;T Gale Power Services — Business Card</title>
<link rel="stylesheet" href="https://fonts.googleapis.com/css2?family=Arimo:wght@400;700&display=swap">
<style>
  :root {
    --page-bg: #e4e0da;
    --card-light: #f7f3ec;
    --card-warm: #ece2d4;
    --brand-green: #1f8a2c;
    --accent-orange: #e8730f;
    --accent-blue: #0677ba;
    --text-dark: #3a3a3a;
    --icon-orange: #e0731a;
  }
  * { box-sizing: border-box; margin: 0; padding: 0; }
  html, body {
    width: 1200px;
    height: 927px;
    overflow: hidden;
    background: var(--page-bg);
    font-family: "Arimo", Arial, sans-serif;
  }
  .business-card {
    position: absolute;
    left: 60px;
    top: 162px;
    width: 1080px;
    height: 603px;
    background: linear-gradient(100deg, var(--card-warm) 0%, var(--card-light) 45%, var(--card-warm) 100%);
    border-radius: 3px;
    box-shadow: 0 6px 22px rgba(0,0,0,0.18);
    overflow: hidden;
  }
  .company-name {
    position: absolute;
    left: 50px;
    top: 72px;
    color: var(--brand-green);
    font-weight: 700;
    font-size: 36px;
    line-height: 1.1;
    letter-spacing: 4px;
    text-transform: uppercase;
  }
  .company-name .line { display: block; }
  .company-name .line.small { font-size: 21px; letter-spacing: 5px; margin-top: 4px; }
  .person-name {
    position: absolute;
    left: 50px;
    top: 282px;
    color: var(--accent-orange);
    font-weight: 700;
    font-size: 42px;
    text-transform: uppercase;
    letter-spacing: -0.5px;
  }
  .address {
    position: absolute;
    left: 50px;
    top: 352px;
    color: var(--text-dark);
    font-size: 26px;
    line-height: 32px;
  }
  .contact-list {
    position: absolute;
    left: 50px;
    top: 436px;
    list-style: none;
    color: var(--text-dark);
    font-size: 26px;
  }
  .contact-list li {
    display: flex;
    align-items: center;
    height: 35px;
  }
  .contact-list svg {
    width: 26px;
    height: 26px;
    margin-right: 15px;
    flex: none;
  }
  .brand-symbol-area {
    position: absolute;
    left: 479px;
    top: 7px;
    width: 584px;
    height: 584px;
    border-radius: 50%;
    background: radial-gradient(circle at 50% 50%, rgba(232,241,248,0.6) 0%, rgba(123,173,215,0.35) 45%, rgba(240,145,44,0.22) 75%, rgba(31,138,44,0.22) 100%);
  }
</style>
</head>
<body>
  <main class="business-card">
    <h1 class="company-name">
      <span class="line">R&amp;T Gale</span>
      <span class="line small">Power Services</span>
    </h1>

    <h2 class="person-name">Dean Whitlock</h2>

    <address class="address">
      318276 Fallow Line #7<br>
      Marrowby, ON X9Z 4Q2
    </address>

    <ul class="contact-list">
      <li>
        <svg viewBox="0 0 24 24" aria-hidden="true"><path fill="var(--icon-orange)" d="M6.6 10.8c1.4 2.8 3.8 5.1 6.6 6.6l2.2-2.2c.3-.3.7-.4 1-.2 1.1.4 2.3.6 3.6.6.6 0 1 .4 1 1V20c0 .6-.4 1-1 1C10.6 21 3 13.4 3 4c0-.6.4-1 1-1h3.5c.6 0 1 .4 1 1 0 1.3.2 2.5.6 3.6.1.3 0 .7-.2 1z"/></svg>
        <span>555-384-9162</span>
      </li>
      <li>
        <svg viewBox="0 0 24 24" aria-hidden="true"><rect x="2" y="5" width="20" height="14" fill="var(--icon-orange)"/><path d="M2 5l10 8 10-8" fill="none" stroke="#f7f3ec" stroke-width="1.6"/></svg>
        <span>DeanWhitlock@randtgale.net</span>
      </li>
      <li>
        <svg viewBox="0 0 24 24" aria-hidden="true"><circle cx="12" cy="12" r="10" fill="var(--icon-orange)"/><path d="M2 12h20M12 2c3 3 3 17 0 20M12 2c-3 3-3 17 0 20" fill="none" stroke="#f7f3ec" stroke-width="1.3"/></svg>
        <span>www.randtgale.net</span>
      </li>
    </ul>

    <div class="brand-symbol-area" role="img" aria-label="Large company brand symbol in orange, green and blue"></div>
  </main>
</body>
</html>
```